Kelvo Roofing & construction LLC

I need an interactive website for potential customers with roofing products that we install and information about the products we install. I also want a page where customers can write reviews through google and facebook and can also contact us at. I would also like to add more information with the winning designer and would pay more with the winning designer.

```html
<!DOCTYPE html>
<html lang="en">
<head>
<meta charset="utf-8">
<title>Kelvo Roofing &amp; construction LLC</title>
<link href="https://fonts.googleapis.com/css2?family=Poppins:ital,wght@0,400;0,500;0,600;0,700;0,800;1,400&display=swap" rel="stylesheet">
<style>
:root{
  --red:#f70f0f;
  --black:#0b0b0b;
  --ink:#151515;
  --grey:#6b6b6b;
  --line:#e4e4e4;
  --white:#ffffff;
  --soft:#f6f6f6;
}
*{box-sizing:border-box;margin:0;padding:0}
html,body{width:1200px;height:4797px;overflow:hidden}
body{position:relative;background:var(--white);font-family:'Poppins',sans-serif;color:var(--ink)}
.abs{position:absolute}
.btn{position:absolute;background:var(--red);color:var(--white);font-weight:600;font-size:18px;display:flex;align-items:center;justify-content:center;letter-spacing:.3px}
.center{text-align:center}

.topbar{left:0;top:0;width:1200px;height:37px;background:var(--red);color:var(--white);font-size:15px;font-weight:500}
.topbar .mail{left:76px;top:8px;display:flex;gap:10px;align-items:center}
.topbar .phone{right:78px;top:8px;display:flex;gap:10px;align-items:center}
.nav{left:0;top:37px;width:1200px;height:88px;background:var(--white)}
.nav a{position:absolute;top:37px;font-size:13.5px;font-weight:500;color:var(--ink);text-decoration:none}
.nav a.active{color:var(--red)}
.brand-tab{left:466px;top:28px;width:268px;height:112px;background:var(--white);clip-path:polygon(8% 0,92% 0,100% 50%,92% 100%,8% 100%,0 50%);display:flex;flex-direction:column;align-items:center;justify-content:center;z-index:3}
.brand-tab .name{font-size:30px;font-weight:700;color:var(--red);line-height:1;letter-spacing:1px}
.brand-tab .sub{font-size:10px;font-weight:500;color:var(--red);letter-spacing:1.5px;margin-top:6px}

.hero{left:0;top:125px;width:1200px;height:551px;background:linear-gradient(180deg,#4a4f55 0%,#3b4046 45%,#2d3a2c 100%)}
.hero-shade{left:0;top:125px;width:1200px;height:551px;background:rgba(0,0,0,.35)}
.hero .kicker{left:0;width:1200px;top:173px;font-size:21px;color:var(--white)}
.hero h1{left:0;width:1200px;top:210px;font-size:43px;line-height:54px;font-weight:800;color:var(--white)}
.hero-arrow{width:50px;height:50px;border:1.5px solid rgba(255,255,255,.7);border-radius:50%;display:flex;align-items:center;justify-content:center}

.eyebrow{font-size:16px;color:var(--red);font-weight:500}
.h2{font-size:40px;font-weight:700;color:var(--ink)}
.body{font-size:14.5px;line-height:27px;color:var(--grey)}

.card{position:absolute;top:1485px;width:322px;height:331px;background:var(--white);border:1px solid #efefef;box-shadow:0 0 12px rgba(0,0,0,.06)}
.card-tip{position:absolute;top:1416px;width:160px;height:130px;background:var(--white);clip-path:polygon(50% 0,100% 100%,0 100%);filter:drop-shadow(0 0 6px rgba(0,0,0,.1))}
.card-tip.down{clip-path:polygon(0 0,100% 0,50% 100%)}
.card h3{position:absolute;left:0;width:100%;top:105px;text-align:center;font-size:17px;font-weight:600}
.card p{position:absolute;left:20px;right:20px;top:146px;text-align:center;font-size:13.5px;line-height:27px;color:var(--grey)}
.card .more{position:absolute;left:0;width:100%;top:258px;text-align:center;font-size:14px;color:var(--red);text-decoration:underline}
.card .nudge{position:absolute;top:310px;width:42px;height:40px;background:var(--black);display:flex;align-items:center;justify-content:center}
.card .nudge.hot{background:var(--red)}

.tile{position:absolute;width:296px;height:312px;border-radius:6px}

.field{position:absolute;height:56px;border:1px solid var(--line);background:rgba(255,255,255,.9);font-size:14px;color:var(--grey);padding:18px 14px}
.field.focus{border-color:var(--red);color:var(--red)}
.info-icon{position:absolute;top:4566px;width:52px;height:52px;border-radius:50%;display:flex;align-items:center;justify-content:center}
.info-text{position:absolute;top:4642px;width:240px;text-align:center;font-size:14px;line-height:24px;color:var(--ink)}
.footer{left:0;top:4738px;width:1200px;height:59px;background:var(--red);color:var(--white);font-size:14px;display:flex;align-items:center;justify-content:center}
</style>
</head>
<body>

<div class="abs topbar">
  <div class="abs mail">
    <svg width="20" height="15" viewBox="0 0 20 15"><rect x="0" y="0" width="20" height="15" rx="2" fill="#fff"/><path d="M1 1l9 7 9-7" stroke="#f70f0f" stroke-width="2" fill="none"/></svg>
    info@kelvo.com
  </div>
  <div class="abs phone">
    <svg width="22" height="22" viewBox="0 0 22 22"><circle cx="11" cy="11" r="10" fill="none" stroke="#fff" stroke-width="1.5"/><path d="M7 6c0 5 4 9 9 9l1-2-3-1-1 1c-2-1-3-2-4-4l1-1-1-3z" fill="#fff"/></svg>
    (123) 456 7890
  </div>
</div>

<nav class="abs nav">
  <a class="active" style="left:178px">&#8226; HOME</a>
  <a style="left:266px">ABOUT US</a>
  <a style="left:367px">SERVICES</a>
  <a style="left:739px">PROJECTS</a>
  <a style="left:837px">TESTIMONIALS</a>
  <a style="left:960px">CONTACT</a>
</nav>
<div class="abs brand-tab">
  <div class="name">Kelvo Roofing</div>
  <div class="sub">&amp; CONSTRUCTION LLC</div>
</div>

<section>
  <div class="abs hero" role="img" aria-label="Photo of a large two-storey house with grey shingle roof at dusk"></div>
  <div class="abs hero-shade"></div>
  <div class="hero">
    <div class="abs kicker center">High Quality Work</div>
    <h1 class="abs center">WE WILL HELP YOU TO<br>FIX YOUR ROOF</h1>
  </div>
  <div class="btn" style="left:449px;top:453px;width:302px;height:54px">GET FREE CONSULTATION</div>
  <div class="abs hero-arrow" style="left:11px;top:361px"><svg width="12" height="18"><path d="M10 2L3 9l7 7" stroke="#fff" stroke-width="1.5" fill="none"/></svg></div>
  <div class="abs hero-arrow" style="left:1134px;top:361px"><svg width="12" height="18"><path d="M2 2l7 7-7 7" stroke="#fff" stroke-width="1.5" fill="none"/></svg></div>
</section>

<section>
  <svg class="abs" style="left:0;top:630px" width="1200" height="600" viewBox="0 0 1200 600">
    <polygon points="860,0 1200,0 1200,395 650,480" fill="#f70f0f"/>
    <polygon points="560,480 1200,400 1200,600" fill="#0b0b0b"/>
  </svg>
  <div class="abs" style="left:530px;top:810px;width:560px;height:330px;background:linear-gradient(160deg,#c9722f 0%,#efe0a2 45%,#f3f1ea 100%);border-radius:4px" role="img" aria-label="Illustration of a cream two-storey house with brown roof on rolled blueprints and a white car"></div>
  <div class="abs eyebrow" style="left:78px;top:748px">WELCOME TO</div>
  <div class="abs h2" style="left:78px;top:775px">KELVO ROOFING</div>
  <p class="abs body" style="left:78px;top:845px;width:440px">Lorem Ipsum is simply dummy text of &nbsp;printing and type setting industry. Lorem Ipsum has been the industry's standard dummy text ever since the 1500s, when an unknown Lorem Ipsum is simply dummy text of &nbsp;printing and typesetting industry Lorem Ipsum is simply dummy. .</p>
  <p class="abs body" style="left:78px;top:1000px;width:440px">Lorem Ipsum is simply dummy text of &nbsp;printing and typesetting industry. Lorem Ipsum has been the industry's standard dummy text ever since the 1500s,</p>
  <div class="btn" style="left:77px;top:1101px;width:182px;height:55px">LEARN MORE</div>
</section>

<section>
  <div class="abs h2 center" style="left:0;width:1200px;top:1297px">OUR SERVICES</div>
  <div class="abs center" style="left:0;width:1200px;top:1356px;font-size:14.5px;color:var(--grey)">Lorem Ipsum is simply dummy text of &nbsp;printing and typesetting.</div>

  <div class="card-tip" style="left:169px"></div>
  <div class="card" style="left:88px">
    <h3>ROOFING</h3>
    <p>Lorem Ipsum is simply dummy text of &nbsp;printing and typesetting industry. Lorem Ipsum has been.</p>
    <div class="more">Read More</div>
    <div class="nudge" style="left:133px"><svg width="10" height="14"><path d="M8 1L2 7l6 6" stroke="#fff" fill="none" stroke-width="1.5"/></svg></div>
  </div>
  <svg class="abs" style="left:222px;top:1476px" width="70" height="54" viewBox="0 0 70 54"><path d="M6 22L30 4l30 18" stroke="#151515" stroke-width="2.5" fill="none"/><path d="M22 16l14 26 22-8-14-26z" fill="#f70f0f"/><path d="M12 26v22M48 34v14" stroke="#151515" stroke-width="2.5"/></svg>

  <div class="card-tip down" style="left:519px;top:1426px"></div>
  <div class="card" style="left:438px">
    <h3 style="color:var(--red)">REMODELING</h3>
    <p>Lorem Ipsum is simply dummy text of &nbsp;printing and typesetting industry. Lorem Ipsum has been.</p>
    <div class="more">Read More</div>
    <div class="nudge hot" style="left:140px"><svg width="10" height="14"><path d="M8 1L2 7l6 6" stroke="#fff" fill="none" stroke-width="1.5"/></svg></div>
  </div>
  <svg class="abs" style="left:571px;top:1420px" width="60" height="60" viewBox="0 0 60 60"><path d="M4 28L30 6l26 22" stroke="#f70f0f" stroke-width="3" fill="none"/><rect x="12" y="26" width="36" height="28" fill="none" stroke="#151515" stroke-width="2.5"/><circle cx="30" cy="40" r="7" fill="none" stroke="#151515" stroke-width="2.5"/></svg>

  <div class="card-tip" style="left:872px"></div>
  <div class="card" style="left:792px">
    <h3>CONSTRUCTION</h3>
    <p>Lorem Ipsum is simply dummy text of &nbsp;printing and typesetting industry. Lorem Ipsum has been.</p>
    <div class="more">Read More</div>
    <div class="nudge" style="left:144px"><svg width="10" height="14"><path d="M8 1L2 7l6 6" stroke="#fff" fill="none" stroke-width="1.5"/></svg></div>
  </div>
  <svg class="abs" style="left:912px;top:1474px" width="72" height="56" viewBox="0 0 72 56"><path d="M4 26L28 8l24 18" stroke="#151515" stroke-width="2.5" fill="none" stroke-dasharray="5 3"/><rect x="12" y="26" width="32" height="26" fill="none" stroke="#151515" stroke-width="2.5"/><rect x="42" y="30" width="18" height="22" fill="#f70f0f"/></svg>
</section>

<section>
  <svg class="abs" style="left:0;top:1930px" width="1200" height="580" viewBox="0 0 1200 580">
    <polygon points="0,0 200,80 560,330 0,460" fill="#0b0b0b"/>
    <polygon points="0,460 560,330 300,510 0,580" fill="#f70f0f"/>
  </svg>
  <div class="abs" style="left:56px;top:2003px;width:531px;height:437px;background:linear-gradient(160deg,#8a4a33 0%,#e58b5d 50%,#f0b28c 100%);border-radius:6px" role="img" aria-label="Illustration of a house cutaway showing roof truss framing and brick walls"></div>
  <div class="abs center" style="left:590px;width:480px;top:2092px;font-size:23px;line-height:34px;font-weight:600">If You Find a High Quality Roofing And<br>Construction For Your Projects</div>
  <div class="abs center" style="left:590px;width:480px;top:2180px;font-size:34px;color:var(--red)">123 456 7890</div>
  <div class="btn" style="left:676px;top:2252px;width:302px;height:56px">GET FREE CONSULTATION</div>
</section>

<section>
  <div class="abs eyebrow center" style="left:0;width:1200px;top:2470px;font-size:15px">OUR WORK</div>
  <div class="abs h2 center" style="left:0;width:1200px;top:2500px">OUR PROJECTS</div>
  <div class="tile" style="left:136px;top:2590px;background:linear-gradient(180deg,#2a2a2a,#3a3530)" role="img" aria-label="Project photo of a dark brick house at night"></div>
  <div class="abs" style="left:248px;top:2709px;width:72px;height:72px;border-radius:50%;background:var(--red);display:flex;align-items:center;justify-content:center"><svg width="34" height="34"><path d="M17 2v30M2 17h30" stroke="#fff" stroke-width="2"/></svg></div>
  <div class="tile" style="left:453px;top:2590px;background:linear-gradient(180deg,#c8d8e8 0%,#8b9098 50%,#5d7a45 100%)" role="img" aria-label="Project photo of a grey house with driveway"></div>
  <div class="tile" style="left:769px;top:2590px;background:linear-gradient(200deg,#9fc3e8 0%,#2f3338 55%,#c2532a 100%)" role="img" aria-label="Project photo of a black tiled roof on a brick house"></div>
  <div class="tile" style="left:136px;top:2927px;background:linear-gradient(180deg,#7fb3e4 0%,#c9896a 55%,#4b6b36 100%)" role="img" aria-label="Project photo of a villa with terracotta roof and palm trees"></div>
  <div class="tile" style="left:453px;top:2927px;background:linear-gradient(200deg,#8fc0ec 0%,#c9302a 50%,#f0f0f0 100%)" role="img" aria-label="Project photo of a white house with red roof tiles"></div>
  <div class="tile" style="left:769px;top:2927px;background:linear-gradient(180deg,#86b8e8 0%,#a56650 50%,#3f6a2f 100%)" role="img" aria-label="Project photo of a brick and white house with garden"></div>
  <div class="btn" style="left:496px;top:3268px;width:208px;height:56px">EXPLORE MORE</div>
</section>

<section>
  <div class="abs" style="left:0;top:3370px;width:640px;height:630px;background:linear-gradient(180deg,rgba(240,240,240,.0),#f4f4f4)"></div>
  <svg class="abs" style="left:640px;top:3410px" width="560" height="600" viewBox="0 0 560 600">
    <polygon points="260,0 560,0 560,520 10,440" fill="#f70f0f"/>
    <polygon points="10,440 560,520 560,590" fill="#0b0b0b"/>
  </svg>
  <div class="abs" style="left:755px;top:3353px;width:353px;height:640px;background:linear-gradient(180deg,#f2c219 0%,#d6ad8c 20%,#2d3e58 55%,#c99a3a 100%);border-radius:8px" role="img" aria-label="Photo of a smiling construction worker in a yellow hard hat holding a level"></div>
  <svg class="abs" style="left:75px;top:3440px" width="66" height="60" viewBox="0 0 66 60"><path d="M28 6C12 12 4 24 4 38a14 14 0 1 0 14-14c2-8 6-12 14-16zM62 6C46 12 38 24 38 38a14 14 0 1 0 14-14c2-8 6-12 14-16z" fill="#f70f0f"/></svg>
  <div class="abs h2" style="left:152px;top:3440px;font-size:40px">TESTIMONIALS</div>
  <div class="abs" style="left:158px;top:3498px;font-size:14px;color:var(--grey)">What Our Client Say About Us</div>
  <div class="abs" style="left:125px;top:3560px;width:116px;height:116px;border-radius:50%;background:linear-gradient(160deg,#8a5a3a,#d9b9a0);border:4px solid #fff" role="img" aria-label="Client portrait"></div>
  <p class="abs" style="left:263px;top:3570px;width:390px;font-size:14px;line-height:27px;font-style:italic;color:var(--grey)">" Lorem Ipsum is simply dummy text of the printing and typesetting industry. Lorem Ipsum has been the industry's standard dummy Lorem Ipsum is simply dummy text of the printing and."</p>
  <div class="abs" style="left:267px;top:3714px;font-size:18px;font-weight:600">CLIENT NAME</div>
  <div class="abs" style="left:267px;top:3742px;font-size:14.5px;color:var(--red)">Something.com</div>
  <div class="abs" style="left:263px;top:3802px;width:50px;height:50px;border-radius:50%;border:1.5px solid var(--red);display:flex;align-items:center;justify-content:center"><svg width="12" height="18"><path d="M10 2L3 9l7 7" stroke="#f70f0f" stroke-width="1.8" fill="none"/></svg></div>
  <div class="abs" style="left:323px;top:3802px;width:50px;height:50px;border-radius:50%;border:1.5px solid var(--ink);display:flex;align-items:center;justify-content:center"><svg width="12" height="18"><path d="M2 2l7 7-7 7" stroke="#151515" stroke-width="1.8" fill="none"/></svg></div>
</section>

<section>
  <div class="abs" style="left:0;top:4300px;width:1200px;height:438px;background:linear-gradient(180deg,#ffffff 0%,#f3f3f3 100%)"></div>
  <div class="abs h2 center" style="left:0;width:1200px;top:4030px">CONTACT US</div>
  <div class="abs center" style="left:0;width:1200px;top:4085px;font-size:19px;color:var(--red)">We'd love to hear from you!</div>
  <div class="abs center" style="left:330px;width:540px;top:4122px;font-size:14px;line-height:27px;color:var(--grey)">Have a question about our services? Want to see if your particular project is one we can help with?</div>
  <div class="field focus" style="left:203px;top:4203px;width:395px">Name *</div>
  <div class="field" style="left:615px;top:4203px;width:395px">Phone *</div>
  <div class="field" style="left:203px;top:4274px;width:395px">Email *</div>
  <div class="field" style="left:615px;top:4274px;width:395px">Services*
    <svg class="abs" style="right:14px;top:24px" width="14" height="8"><path d="M0 0h14L7 8z" fill="#151515"/></svg></div>
  <div class="field" style="left:203px;top:4344px;width:807px;height:97px">Message*</div>
  <div class="btn" style="left:490px;top:4462px;width:218px;height:54px">SEND A MESSAGE</div>

  <div class="info-icon" style="left:300px;background:var(--red)"><svg width="20" height="26"><path d="M10 1a8 8 0 0 0-8 8c0 6 8 15 8 15s8-9 8-15a8 8 0 0 0-8-8z" fill="none" stroke="#fff" stroke-width="2"/><circle cx="10" cy="9" r="3" fill="#fff"/></svg></div>
  <div class="info-text" style="left:200px">101- Loremipsum simple<br>text print address.</div>
  <div class="info-icon" style="left:572px;background:var(--black)"><svg width="22" height="22"><path d="M5 3c0 8 6 14 14 14l1-3-4-2-2 2c-3-1-5-3-6-6l2-2-2-4z" fill="#f70f0f"/></svg></div>
  <div class="info-text" style="left:478px">Phone :<br>+(1) 123 466 7890</div>
  <div class="info-icon" style="left:844px;background:var(--black)"><svg width="22" height="16"><rect x="1" y="1" width="20" height="14" fill="#f70f0f"/><path d="M1 1l10 8 10-8" stroke="#0b0b0b" stroke-width="1.5" fill="none"/></svg></div>
  <div class="info-text" style="left:760px">Email :<br>info@kelvo.com</div>
</section>

<footer class="abs footer">&copy;<b>Kelvo Roofing</b>&nbsp;-2020 All rights &nbsp;reserved.</footer>

</body>
</html>
```